Website visual upgrade

I am seeking expressions of interest for the updating the visuals of my website www.lunvaleplacements.example
I am basically seeking a simple,bold and visually strong graphic makeover.using existing or shortly to be modified text.

```html
<!DOCTYPE html>
<html lang="en">
<head>
<meta charset="utf-8">
<title>Lunvale Placements</title>
<link href="https://fonts.googleapis.com/css2?family=Oswald:wght@400&family=Lato:wght@400;700&family=Roboto:wght@400;500&display=swap" rel="stylesheet">
<style>
:root{
  --red:#b8172f;
  --red-bright:#d01d38;
  --ink:#2b2b2b;
  --grey:#555;
  --light:#f2f2f2;
  --footer:#333333;
  --nav-top:#5a5a5a;
  --nav-bottom:#2e2e2e;
  --white:#fff;
}
*{margin:0;padding:0;box-sizing:border-box}
html,body{width:1146px;height:1200px;overflow:hidden}
body{position:relative;background:var(--white);font-family:'Lato',sans-serif;color:var(--grey)}
.top-rule{position:absolute;left:0;top:0;width:100%;height:5px;background:#222}
.header{position:absolute;left:0;top:5px;width:100%;height:126px;background:var(--light)}
.hero-band{position:absolute;left:0;top:131px;width:100%;height:396px;background:var(--red)}
.brand{position:absolute;left:127px;top:42px;display:flex;align-items:center;gap:12px}
.brand-mark{width:34px;height:34px;border-radius:50%;background:var(--ink)}
.brand-name{font-family:'Roboto',sans-serif;font-weight:500;font-size:32px;color:var(--red);letter-spacing:.5px}
.follow{position:absolute;left:836px;top:52px;display:flex;align-items:center;gap:6px;font-size:13px;color:var(--red-bright)}
.follow span{margin-right:4px}
.social{width:24px;height:24px;border-radius:3px}
.s1{background:#3b5b9a}.s2{background:#4bb6dc}.s3{background:#1d75b2}.s4{background:#f08a1c}
.nav{position:absolute;left:115px;top:109px;width:917px;height:43px;border-radius:4px;background:linear-gradient(var(--nav-top),var(--nav-bottom));display:flex;align-items:center;justify-content:space-around;padding:0 6px}
.nav a{font-family:'Roboto',sans-serif;font-size:11.5px;color:#fff;text-decoration:none;letter-spacing:.4px}
.slider{position:absolute;left:115px;top:164px;width:917px;height:339px;background:#fff;padding:5px}
.slide{width:100%;height:100%;background:linear-gradient(90deg,#c9c6bd 0%,#d88a55 30%,#a9a59a 55%,#8d8a82 100%)}
.caption{position:absolute;left:488px;top:112px;width:424px;height:117px;background:rgba(245,245,245,.82);padding:6px 0 0 22px;font-family:'Roboto',sans-serif;font-weight:500;font-size:50px;line-height:50px;color:#262626;letter-spacing:.5px}
.arrows{position:absolute;left:539px;top:486px;display:flex;gap:9px}
.arrow{width:30px;height:30px}
.welcome{position:absolute;left:0;top:558px;width:100%;text-align:center}
.welcome h1{font-family:'Oswald',sans-serif;font-weight:400;font-size:29px;color:var(--red)}
.welcome p{width:900px;margin:10px auto 0;font-size:15px;line-height:22px;color:#555}
.card{position:absolute;top:691px;width:287px;height:345px;background:#fff;box-shadow:0 2px 5px rgba(0,0,0,.15);text-align:center}
.card h2{height:43px;background:var(--red-bright);color:#fff;font-family:'Oswald',sans-serif;font-weight:400;font-size:24px;line-height:43px;border-radius:3px 3px 0 0}
.card-photo{display:block;width:287px;height:155px}
.card p{font-size:12px;line-height:22px;color:#555;padding:16px 12px 0}
.card .more{display:block;margin-top:8px;font-size:12px;color:#222}
.footer{position:absolute;left:0;top:1067px;width:100%;height:133px;background:var(--footer);color:#ddd;font-size:11.5px}
.footer-links{position:absolute;left:124px;top:braces;}
.footer-links{top:27px;letter-spacing:.3px}
.footer-links i{font-style:normal;margin:0 8px}
.copy{position:absolute;left:124px;top:67px;line-height:25px}
.copy b{font-weight:400;color:#f03c58}
.support{position:absolute;left:820px;top:22px;font-size:14px;color:#fff}
.badge{position:absolute;top:50px;height:55px}
.badge-a{left:820px;width:133px;background:#fff}
.badge-b{left:970px;width:51px;background:#111}
</style>
</head>
<body>
<div class="top-rule"></div>
<div class="header"></div>
<div class="hero-band"></div>

<div class="brand"><span class="brand-mark"></span><span class="brand-name">Lunvale Placements</span></div>
<div class="follow"><span>Follow Us :</span><i class="social s1"></i><i class="social s2"></i><i class="social s3"></i><i class="social s4"></i></div>

<nav class="nav">
  <a href="#">HOME</a><a href="#">WHO WE ARE</a><a href="#">OUR APPROACH</a><a href="#">WHAT WE DO</a><a href="#">MIGRATION ASSISTANCE</a><a href="#">JOB SEEKERS</a><a href="#">USEFUL LINKS</a><a href="#">SUPPORT</a><a href="#">CONTACT US</a>
</nav>

<div class="slider">
  <div class="slide" role="img" aria-label="Smiling worker in hard hat and high-visibility vest at a mining site"></div>
  <div class="caption">Local Presence,<br>Global Reach</div>
</div>
<div class="arrows">
  <svg class="arrow" viewBox="0 0 30 30"><circle cx="15" cy="15" r="14" fill="#f4f4f4" stroke="#bbb"/><path d="M17 9l-6 6 6 6" fill="none" stroke="#333" stroke-width="3"/></svg>
  <svg class="arrow" viewBox="0 0 30 30"><circle cx="15" cy="15" r="14" fill="#f4f4f4" stroke="#bbb"/><path d="M13 9l6 6-6 6" fill="none" stroke="#333" stroke-width="3"/></svg>
</div>

<section class="welcome">
  <h1>Welcome to Our Site</h1>
  <p>We are committed to providing the highest standards of service in Executive search and selection and the provision of Skilled trades people and allied Health professionals throughout Australia.</p>
</section>

<article class="card" style="left:124px">
  <h2>Who We Are</h2>
  <svg class="card-photo" role="img" aria-label="Group of smiling business professionals"><rect width="287" height="155" fill="#b9bcc0"/><path d="M118 0l25 14 25-14z" fill="#d01d38"/></svg>
  <p>Aliquam molestie, mi et imperdiet euismod, dui purus auctor tellus, et interdum lacus lectus et ante. Sed accumsan sollicitudin sapien, sit amet adipiscing turpis gravida ac.</p>
  <a class="more">&lt;&lt; READ MORE &gt;&gt;</a>
</article>
<article class="card" style="left:430px">
  <h2>What We Do</h2>
  <svg class="card-photo" role="img" aria-label="Business meeting discussion"><rect width="287" height="155" fill="#a7afba"/><path d="M118 0l25 14 25-14z" fill="#d01d38"/></svg>
  <p>Aliquam molestie, mi et imperdiet euismod, dui purus auctor tellus, et interdum lacus lectus et ante. Sed accumsan sollicitudin sapien, sit amet adipiscing turpis gravida ac.</p>
  <a class="more">&lt;&lt; READ MORE &gt;&gt;</a>
</article>
<article class="card" style="left:735px">
  <h2>Our Approach</h2>
  <svg class="card-photo" role="img" aria-label="Hand moving a chess piece"><rect width="287" height="155" fill="#4a4038"/><path d="M118 0l25 14 25-14z" fill="#d01d38"/></svg>
  <p>Aliquam molestie, mi et imperdiet euismod, dui purus auctor tellus, et interdum lacus lectus et ante. Sed accumsan sollicitudin sapien, sit amet adipiscing turpis gravida ac.</p>
  <a class="more">&lt;&lt; READ MORE &gt;&gt;</a>
</article>

<footer class="footer">
  <div class="footer-links">Home<i>|</i>Contact Us<i>|</i>Privacy Policy<i>|</i>Site Map</div>
  <div class="copy">Copyright ©2013. <b>Lunvale Placements</b><br>All Right Reserved</div>
  <div class="support">Proud to Support</div>
  <div class="badge badge-a"></div>
  <div class="badge badge-b"></div>
</footer>
</body>
</html>
```